Logo and Business Card Design

Harbor Vale Logistics provides our customers with one call solutions to packing, trucking and warehousing needs throughout the supply chain.
We need ideas for a logo/business card. I have 2 general concepts.
1. Modern logo involving: the globe, Harbor Vale, arrow, movement, the two words having 2 different fonts/colors, the number 1.
2. Logo involving Lion/Winged Lion: incorporate lion onto globe, tagline "The Crest of the Herd", movement, flowing.

Target Market(s)

International Logistics companies, Air cargo companies, manufacturing companies

Industry/Entity Type

Business

Contact Information for Business Card

Dale Whitfield
Owner
Harbor Vale Logistics
2874 Maren Ave.
Cedar Hollow Park, OH 43029
555-539-2864
daleh@harborvalefreight.example

Font styles to use
Sans Serif

Requirements
Must have
• 1. Modern logo involving: the globe, Harbor Vale, arrow, movement, the two words having 2 different fonts/colors, the number 1.
Nice to have
Should not have
• Do not have too complex of a design.

```html
<!DOCTYPE html>
<html lang="en">
<head>
<meta charset="utf-8">
<title>Harbor Vale Logistics – Business Cards</title>
<link rel="stylesheet" href="https://fonts.googleapis.com/css2?family=Saira:wght@400;500;700&display=swap">
<style>
  :root {
    --page-bg: #3a3a3c;
    --card-border: #ffffff;
    --card-dark: #231f20;
    --card-blue: #00adef;
    --ink-light: #ffffff;
    --wordmark: #e6e6e6;
  }
  * { margin: 0; padding: 0; box-sizing: border-box; }
  html, body { width: 1200px; height: 1000px; overflow: hidden; }
  body {
    background: var(--page-bg);
    position: relative;
    font-family: "Saira", "Arial", sans-serif;
  }
  .card {
    position: absolute;
    left: 272px;
    width: 700px;
    height: 410px;
    background: var(--card-border);
    padding: 23px;
  }
  .card--dark { top: 88px; }
  .card--blue { top: 530px; }
  .card__face {
    position: relative;
    width: 100%;
    height: 100%;
    border-radius: 8px;
    color: var(--ink-light);
    text-align: center;
  }
  .card--dark .card__face { background: var(--card-dark); }
  .card--blue .card__face { background: var(--card-blue); }
  .brand-mark {
    position: absolute;
    left: 50%;
    top: 34px;
    width: 150px;
    height: 150px;
    margin-left: -75px;
    border-radius: 50%;
    background: var(--ink-light);
  }
  .card__details {
    position: absolute;
    left: 0;
    right: 0;
    top: 192px;
    line-height: 1;
  }
  .wordmark {
    font-size: 28px;
    font-weight: 500;
    color: var(--wordmark);
    height: 30px;
  }
  .address { font-size: 20px; height: 26px; margin-top: 2px; letter-spacing: 0.3px; }
  .person-name { font-size: 20px; font-weight: 700; height: 24px; margin-top: 10px; }
  .person-role { font-size: 21px; height: 25px; }
  .phone { font-size: 22px; height: 23px; letter-spacing: 0.4px; }
  .email { font-size: 20px; height: 24px; letter-spacing: 0.3px; }
</style>
</head>
<body>
  <section class="card card--dark">
    <div class="card__face">
      <div class="brand-mark"></div>
      <div class="card__details">
        <p class="wordmark">Harbor Vale Logistics</p>
        <p class="address">2874 Maren Ave. Cedar Hollow Park, OH</p>
        <p class="person-name">Dale Whitfield</p>
        <p class="person-role">Owner</p>
        <p class="phone">43029 555-539-2864</p>
        <p class="email">daleh@harborvalefreight.example</p>
      </div>
    </div>
  </section>
  <section class="card card--blue">
    <div class="card__face">
      <div class="brand-mark"></div>
      <div class="card__details">
        <p class="wordmark">Harbor Vale Logistics</p>
        <p class="address">2874 Maren Ave. Cedar Hollow Park, OH</p>
        <p class="person-name">Dale Whitfield</p>
        <p class="person-role">Owner</p>
        <p class="phone">43029 555-539-2864</p>
        <p class="email">daleh@harborvalefreight.example</p>
      </div>
    </div>
  </section>
</body>
</html>
```